Re-design of a website for Jewellery Store

We need a design for a jewellery store that will be on Shopify.

The website is going to be on Shopify and we will install a new theme and we need to create new designs, based on a similar layout to the theme so we can simply customise the theme colours and banners etc to fit the layout of the theme.

We have a link of the old website that we need to improve and make better.

We need a slick modern design and can use photos of his jewellery etc.

Here are three themes we think are good for us

https://morvanti-gems.example-shop.com/collections/featured
https://pellwick-01.example-shop.com/
https://vistune-demo.example-shop.com/

Here's a few websites I like the look and function of below with notes. But
open to hearing your opinions and ideas.

https://www.fernandquill.example/ - I like the main page as there is a little
more going on. I also like the layout of the stock pages and how simple this
is to view the jewellery.

https://www.miriamholte.example/nz/jewellery/all-jewellery/harbour-crest-ring-g
old-mh582t4p/gold - I like this website layout the best for stock. I think
it is really simple to view all items. I like best once you click into a
stock piece the layout on the attached link of the individual options and
price options for each piece.

https://tollandpine.example.au/pages/contact-us - I like the contact us page with
more detail the customer has to fill in about what the are enquiring about.

https://www.oritaandbrisk.example.nz/bespoke-designs/ - I like the page
dedicated to "one off" custom designs that we can showcase more like a
gallery separate to our stock in store to give customers ideas if they
wanted to book an appointment to design their own ring.
Updates

Once somebody shows interest I will provide the URL of the old website that we are re-designing to work on.

Target Market(s)

People buying Jewellery

Number of Pages Required

1 page

Font styles to use
Sans Serif

Requirements
Must have
• Must be professional, and a fresher image then what we currently have.

```html
<!DOCTYPE html>
<html lang="en">
<head>
<meta charset="utf-8">
<title>Lunelle Jewellery — Home</title>
<link href="https://fonts.googleapis.com/css2?family=Playfair+Display:wght@400;600;700&family=Lato:wght@300;400;700&display=swap" rel="stylesheet">
<style>
:root{
  --bg:#f4f4f4;
  --page:#ffffff;
  --ink:#2b2b2b;
  --muted:#7a7a7a;
  --line:#e3e3e3;
  --soft:#f1f0f0;
  --accent:#d6a2cc;
  --accent-dark:#b97fae;
  --gold:#c9a64a;
}
*{box-sizing:border-box;margin:0;padding:0}
html,body{width:1200px;height:3156px;overflow:hidden}
body{background:var(--bg);font-family:'Lato',sans-serif;color:var(--ink);font-size:11px}
.page{width:800px;margin:18px auto 0;background:var(--page);box-shadow:0 2px 14px rgba(0,0,0,.06)}
h1,h2,h3{font-family:'Playfair Display',serif;font-weight:600}
.btn{display:inline-block;background:var(--accent);color:#fff;font-size:10px;letter-spacing:.08em;text-transform:uppercase;padding:8px 18px;border-radius:2px;white-space:nowrap}
.btn-outline{display:inline-block;border:1px solid var(--ink);color:var(--ink);font-size:9px;letter-spacing:.08em;text-transform:uppercase;padding:7px 14px;margin-right:8px;white-space:nowrap}
.ph{display:block}

/* header */
.site-header{height:62px;display:flex;align-items:center;justify-content:space-between;padding:0 34px;border-bottom:1px solid var(--line)}
.brand{font-family:'Lato',sans-serif;font-weight:700;font-size:12px;letter-spacing:.14em;color:var(--ink);display:flex;align-items:center;gap:6px}
.brand i{width:8px;height:8px;border-radius:50%;background:var(--accent);display:inline-block}
.main-nav{display:flex;gap:26px;font-size:10px;letter-spacing:.06em;text-transform:uppercase}
.header-icons{display:flex;gap:14px}

/* hero */
.hero{position:relative;height:350px;background:var(--soft);display:flex;align-items:center;padding:0 60px}
.hero-copy{width:370px;position:relative;z-index:1}
.hero-copy h1{font-size:30px;line-height:1.2;margin-bottom:12px}
.hero-copy p{color:var(--muted);font-size:12px;margin-bottom:22px}
.hero-image{position:absolute;right:120px;top:0;width:250px;height:350px;background:linear-gradient(180deg,#d9c8bf,#5a4036 55%,#2e2320)}
.slider-arrow{position:absolute;top:164px;width:22px;height:22px;border-radius:50%;background:#fff;display:flex;align-items:center;justify-content:center}
.slider-arrow.prev{left:14px}.slider-arrow.next{right:14px}

/* categories */
.categories{padding:44px 60px 48px}
.section-head{display:flex;justify-content:space-between;align-items:baseline;margin-bottom:24px}
.section-head h2{font-size:20px}
.section-head a{font-size:10px;color:var(--muted)}
.category-grid{display:grid;grid-template-columns:repeat(4,1fr);gap:30px}
.category-card .ph{height:150px;margin-bottom:12px}
.category-card h3{font-size:13px;text-align:center;font-weight:400}

/* products */
.products{padding:14px 48px 56px;text-align:center}
.center-title{font-size:17px;letter-spacing:.08em;text-transform:uppercase;margin-bottom:10px}
.lead{color:var(--muted);font-size:10px;line-height:1.6;width:460px;margin:0 auto 24px}
.product-row{position:relative;display:grid;grid-template-columns:repeat(4,1fr);gap:18px;padding:0 22px}
.product-card{border:1px solid var(--line);padding:12px;text-align:left;position:relative}
.product-card .tag{position:absolute;top:8px;left:8px;background:var(--accent);color:#fff;font-size:8px;padding:2px 6px}
.product-card .ph{height:130px;background:#fafafa;margin-bottom:10px;border:1px solid #f0f0f0}
.product-card h3{font-family:'Lato',sans-serif;font-size:10px;font-weight:700;letter-spacing:.06em;text-transform:uppercase;margin-bottom:4px}
.product-card .price{color:var(--muted);font-size:10px;margin-bottom:8px}
.field{border:1px solid var(--line);height:20px;font-size:9px;color:var(--muted);padding:4px 6px;margin-bottom:6px;display:flex;justify-content:space-between}
.qty-row{display:flex;justify-content:space-between;font-size:9px;color:var(--muted);margin:8px 0}
.product-card .btn{font-size:8px;padding:6px 10px}
.row-arrow{position:absolute;top:150px;font-size:14px;color:var(--muted)}
.row-arrow.prev{left:0}.row-arrow.next{right:0}

/* feature */
.feature{background:var(--soft);height:360px;position:relative;padding:34px 80px}
.feature-image{width:210px;height:292px;background:linear-gradient(160deg,#b57358,#5c3626 60%,#2a1a14)}
.feature-card{position:absolute;left:270px;top:80px;width:360px;background:#fff;padding:26px 28px;box-shadow:0 4px 16px rgba(0,0,0,.06)}
.feature-card h2{font-size:16px;line-height:1.3;margin-bottom:10px}
.feature-card p{font-size:10px;color:var(--muted);line-height:1.6;margin-bottom:8px}
.feature-card li{list-style:none;font-size:10px;color:var(--muted);margin-bottom:14px}

/* build your own */
.build{display:flex;align-items:center;justify-content:space-between;padding:40px 80px;height:300px}
.build-copy{width:300px}
.build-copy h2{font-size:24px;margin-bottom:12px}
.build-copy p{font-size:10px;color:var(--muted);line-height:1.6;margin-bottom:8px}
.build-copy .strong{color:var(--ink);font-weight:700;margin-bottom:16px}
.build-buttons{display:flex;flex-direction:column;gap:8px;align-items:flex-start}
.build-image{width:300px;height:180px;background:linear-gradient(120deg,#f2ead9,#e6c877 45%,#e3a3a8 75%,#f5eee4)}

/* newsletter */
.newsletter{background:var(--soft);height:150px;text-align:center;padding-top:32px}
.newsletter h2{font-size:16px;letter-spacing:.16em;margin-bottom:8px}
.newsletter p{font-size:10px;color:var(--muted);margin-bottom:16px}
.subscribe{display:flex;justify-content:center}
.subscribe .input{width:300px;height:30px;background:#fff;border:1px solid var(--line);font-size:10px;color:var(--muted);padding:9px 12px;text-align:left}
.subscribe .btn{height:30px;border-radius:0}

/* perks */
.perks{height:62px;display:flex;justify-content:space-around;align-items:center;border-bottom:1px solid var(--line);padding:0 60px}
.perk{display:flex;align-items:center;gap:10px;font-size:10px}
.perk-divider{width:1px;height:24px;background:var(--line)}

/* instagram */
.instagram{padding:36px 30px 44px;text-align:center}
.instagram h2{font-size:22px;letter-spacing:.06em;margin-bottom:8px}
.instagram .lead{margin-bottom:8px}
.handle{font-size:9px;color:var(--muted);margin-bottom:20px}
.insta-grid{display:grid;grid-template-columns:repeat(6,1fr);gap:6px;margin-bottom:24px}
.insta-grid .ph{height:150px}

/* testimonials */
.testimonials{padding:14px 80px 50px;text-align:center}
.testimonials h2{font-size:18px;letter-spacing:.14em;margin-bottom:28px}
.testimonial{display:flex;gap:50px;align-items:center;text-align:left}
.testimonial .ph{width:280px;height:200px;background:linear-gradient(150deg,#e9dfda,#b98f86 55%,#6d4b45)}
.quote{font-size:12px;line-height:1.7;width:300px}
.quote .name{font-weight:700;margin:14px 0 6px}
.stars{display:flex;gap:3px}
.t-arrows{display:flex;gap:6px;margin-top:14px}
.t-arrows span{width:20px;height:20px;border:1px solid var(--line);display:flex;align-items:center;justify-content:center}

/* footer */
.site-footer{background:var(--soft);padding:40px 60px 0}
.footer-cols{display:grid;grid-template-columns:1.4fr 1fr 1fr 1.2fr;gap:30px;padding-bottom:36px}
.site-footer h4{font-size:10px;letter-spacing:.1em;text-transform:uppercase;margin-bottom:12px}
.site-footer p,.site-footer li{font-size:9px;color:var(--muted);line-height:1.8;list-style:none}
.socials{display:flex;gap:8px;margin-top:12px}
.socials i{width:14px;height:14px;border-radius:50%;background:var(--ink);display:inline-block}
.contact-line{display:flex;align-items:center;gap:8px;font-size:10px;margin-bottom:10px}
.phone{font-size:14px;font-weight:700;margin-bottom:12px}
.copyright{border-top:1px solid var(--line);text-align:center;font-size:8px;color:var(--muted);padding:14px 0}
</style>
</head>
<body>
<div class="page">

  <header class="site-header">
    <div class="brand"><i></i>LUNELLE JEWELLERY</div>
    <nav class="main-nav"><span>Home</span><span>Shop</span><span>About</span><span>Blog</span><span>Contact</span></nav>
    <div class="header-icons">
      <svg width="12" height="12" viewBox="0 0 12 12" fill="none" stroke="#2b2b2b"><circle cx="5" cy="5" r="3.8"/><path d="M8 8l3 3"/></svg>
      <svg width="12" height="12" viewBox="0 0 12 12" fill="none" stroke="#2b2b2b"><circle cx="6" cy="4" r="2.5"/><path d="M1.5 11.5c.5-3 2.5-4 4.5-4s4 1 4.5 4"/></svg>
      <svg width="12" height="12" viewBox="0 0 12 12" fill="none" stroke="#2b2b2b"><path d="M2 4h8l-1 7H3z"/><path d="M4 4V3a2 2 0 0 1 4 0v1"/></svg>
    </div>
  </header>

  <section class="hero">
    <div class="hero-copy">
      <h1>Stylish Jewelry That Won't Cost Half Your Paycheck</h1>
      <p>Enjoy the season in these looks</p>
      <span class="btn">Shop Now</span>
    </div>
    <div class="hero-image ph" role="img" aria-label="Model with long dark hair wearing gold rings and earrings"></div>
    <span class="slider-arrow prev"><svg width="8" height="8" viewBox="0 0 8 8"><path d="M5.5 1L2.5 4l3 3" fill="none" stroke="#2b2b2b"/></svg></span>
    <span class="slider-arrow next"><svg width="8" height="8" viewBox="0 0 8 8"><path d="M2.5 1l3 3-3 3" fill="none" stroke="#2b2b2b"/></svg></span>
  </section>

  <section class="categories">
    <div class="section-head"><h2>Shop by Category</h2><a>Explore more products →</a></div>
    <div class="category-grid">
      <div class="category-card"><div class="ph" role="img" aria-label="Gold bracelets on a wrist" style="background:linear-gradient(140deg,#e8c9a6,#b98a5c)"></div><h3>Bracelets</h3></div>
      <div class="category-card"><div class="ph" role="img" aria-label="Gold earrings on an ear" style="background:linear-gradient(140deg,#f0d7c6,#c99b83)"></div><h3>Earrings</h3></div>
      <div class="category-card"><div class="ph" role="img" aria-label="Gold necklace against skin" style="background:linear-gradient(140deg,#f3dfd8,#d8a99a)"></div><h3>Necklace</h3></div>
      <div class="category-card"><div class="ph" role="img" aria-label="Stacked gold rings on fingers" style="background:linear-gradient(140deg,#efd4c9,#c98f82)"></div><h3>Rings</h3></div>
    </div>
  </section>

  <section class="products">
    <h2 class="center-title">Step Up Your Ear Game</h2>
    <p class="lead">Dainty hoops, bold studs and everyday drops picked to finish any look. Mix, match and stack your favourite pieces for every occasion.</p>
    <div class="product-row">
      <span class="row-arrow prev">‹</span>
      <div class="product-card"><span class="tag">New</span><div class="ph" role="img" aria-label="Gold pendant necklace product shot"></div><h3>Briella Set</h3><p class="price">$48.00</p><div class="field">Gold<span>⌄</span></div><div class="qty-row"><span>Qty</span><span>− 1 +</span></div><span class="btn">Add to Cart</span></div>
      <div class="product-card"><span class="tag">New</span><div class="ph" role="img" aria-label="Gold hoop earrings product shot"></div><h3>Caprice Hoops</h3><p class="price">$36.00</p><div class="field">Gold<span>⌄</span></div><div class="qty-row"><span>Qty</span><span>− 1 +</span></div><span class="btn">Add to Cart</span></div>
      <div class="product-card"><span class="tag">New</span><div class="ph" role="img" aria-label="Gold stone ring product shot"></div><h3>Nova Ring</h3><p class="price">$42.00</p><div class="field">Size 7<span>⌄</span></div><div class="qty-row"><span>Qty</span><span>− 1 +</span></div><span class="btn">Add to Cart</span></div>
      <div class="product-card"><span class="tag">New</span><div class="ph" role="img" aria-label="Fine gold chain necklace product shot"></div><h3>Solene Chain</h3><p class="price">$54.00</p><div class="field">Gold<span>⌄</span></div><div class="qty-row"><span>Qty</span><span>− 1 +</span></div><span class="btn">Add to Cart</span></div>
      <span class="row-arrow next">›</span>
    </div>
  </section>

  <section class="feature">
    <div class="feature-image ph" role="img" aria-label="Woman with auburn hair wearing layered gold necklaces"></div>
    <div class="feature-card">
      <h2>Amazing, Beautiful Dainty<br>Lira Rings</h2>
      <p>Delicate bands in solid gold and sterling silver, made to be worn alone or stacked together every day.</p>
      <ul><li>— Hand finished in small batches</li></ul>
      <span class="btn">Shop Rings</span>
    </div>
  </section>

  <section class="build">
    <div class="build-copy">
      <h2>Build Your Own Ring</h2>
      <p>Choose your stone, setting and band to create a one-off piece designed around you.</p>
      <p class="strong">Book a free design consultation</p>
      <div class="build-buttons"><span class="btn-outline">Start With a Setting</span><span class="btn-outline">Start With a Stone</span></div>
    </div>
    <div class="build-image ph" role="img" aria-label="Gold ring with a white diamond and a pink gemstone"></div>
  </section>

  <section class="newsletter">
    <h2>SAVE 10% TODAY</h2>
    <p>Join our list and enjoy 10% off your first order, plus early access to new arrivals.</p>
    <div class="subscribe"><span class="input">Enter your email</span><span class="btn">Subscribe</span></div>
  </section>

  <section class="perks">
    <div class="perk"><svg width="18" height="14" viewBox="0 0 18 14" fill="none" stroke="#2b2b2b"><path d="M1 2h10v8H1zM11 5h4l2 3v2h-6"/><circle cx="4" cy="11.5" r="1.5"/><circle cx="14" cy="11.5" r="1.5"/></svg>Free Shipping</div>
    <span class="perk-divider"></span>
    <div class="perk"><svg width="16" height="16" viewBox="0 0 16 16" fill="none" stroke="#2b2b2b"><circle cx="8" cy="8" r="6.5"/><path d="M8 4v4l3 2"/></svg>24/7 Support</div>
    <span class="perk-divider"></span>
    <div class="perk"><svg width="16" height="16" viewBox="0 0 16 16" fill="none" stroke="#2b2b2b"><path d="M3 8a5 5 0 1 0 1.5-3.5M3 2v3h3"/></svg>30 Day Product Returns</div>
  </section>

  <section class="instagram">
    <h2>SHOP OUR INSTAGRAM</h2>
    <p class="lead">Tag us in your favourite pieces for a chance to be featured in our gallery.</p>
    <p class="handle">@lunellejewellery</p>
    <div class="insta-grid">
      <div class="ph" role="img" aria-label="Model in black wearing gold jewellery" style="background:linear-gradient(150deg,#3b3331,#8a7368)"></div>
      <div class="ph" role="img" aria-label="Hands with gold rings" style="background:linear-gradient(150deg,#d9b8a3,#9c735c)"></div>
      <div class="ph" role="img" aria-label="Pink toned jewellery flat lay" style="background:linear-gradient(150deg,#f3d8dc,#e0b4bd)"></div>
      <div class="ph" role="img" aria-label="Pearl earrings on pink background" style="background:linear-gradient(150deg,#f1cbd3,#deaab7)"></div>
      <div class="ph" role="img" aria-label="Soft pink background with ring" style="background:linear-gradient(150deg,#f7e4e4,#ecc9c9)"></div>
      <div class="ph" role="img" aria-label="Hand wearing stacked rings" style="background:linear-gradient(150deg,#f0dcd0,#d4ad98)"></div>
      <div class="ph" role="img" aria-label="Round gold pendant on cream" style="background:linear-gradient(150deg,#f3e7da,#d9bd98)"></div>
      <div class="ph" role="img" aria-label="Gold drop earrings" style="background:linear-gradient(150deg,#efe4da,#caa77a)"></div>
      <div class="ph" role="img" aria-label="Pastel jewellery arrangement" style="background:linear-gradient(150deg,#f6e6e0,#e5c3bb)"></div>
      <div class="ph" role="img" aria-label="Model wearing gold ear cuff" style="background:linear-gradient(150deg,#e7cfc4,#b58c7c)"></div>
      <div class="ph" role="img" aria-label="Gold chain on pale backdrop" style="background:linear-gradient(150deg,#f4ece6,#dcc6b6)"></div>
      <div class="ph" role="img" aria-label="Rings on a dish" style="background:linear-gradient(150deg,#efe2d6,#c9a88c)"></div>
    </div>
    <span class="btn">View More</span>
  </section>

  <section class="testimonials">
    <h2>TESTIMONIALS</h2>
    <div class="testimonial">
      <div class="ph" role="img" aria-label="Customer wearing statement earrings"></div>
      <div class="quote">
        <p>I am just so glad I found you in time for my sister's wedding. The pieces arrived quickly, look even better in person and I get compliments every time I wear them.</p>
        <p class="name">Rowan Ellery, NZ</p>
        <div class="stars">
          <svg width="11" height="11" viewBox="0 0 10 10"><path d="M5 .5l1.3 2.9 3.2.3-2.4 2.1.7 3.1L5 7.3 2.2 8.9l.7-3.1L.5 3.7l3.2-.3z" fill="#d6a2cc"/></svg>
          <svg width="11" height="11" viewBox="0 0 10 10"><path d="M5 .5l1.3 2.9 3.2.3-2.4 2.1.7 3.1L5 7.3 2.2 8.9l.7-3.1L.5 3.7l3.2-.3z" fill="#d6a2cc"/></svg>
          <svg width="11" height="11" viewBox="0 0 10 10"><path d="M5 .5l1.3 2.9 3.2.3-2.4 2.1.7 3.1L5 7.3 2.2 8.9l.7-3.1L.5 3.7l3.2-.3z" fill="#d6a2cc"/></svg>
          <svg width="11" height="11" viewBox="0 0 10 10"><path d="M5 .5l1.3 2.9 3.2.3-2.4 2.1.7 3.1L5 7.3 2.2 8.9l.7-3.1L.5 3.7l3.2-.3z" fill="#d6a2cc"/></svg>
          <svg width="11" height="11" viewBox="0 0 10 10"><path d="M5 .5l1.3 2.9 3.2.3-2.4 2.1.7 3.1L5 7.3 2.2 8.9l.7-3.1L.5 3.7l3.2-.3z" fill="#d6a2cc"/></svg>
        </div>
        <div class="t-arrows"><span>‹</span><span>›</span></div>
      </div>
    </div>
  </section>

  <footer class="site-footer">
    <div class="footer-cols">
      <div>
        <div class="brand" style="margin-bottom:12px"><i></i>LUNELLE JEWELLERY</div>
        <p>Affordable fine jewellery designed to be worn every day, made with care and finished by hand.</p>
        <div class="socials"><i></i><i></i><i></i><i></i></div>
      </div>
      <div>
        <h4>About Us</h4>
        <ul><li>Our Story</li><li>Bespoke Designs</li><li>Journal</li><li>Stockists</li><li>Careers</li></ul>
      </div>
      <div>
        <h4>Customer Care</h4>
        <ul><li>Contact Us</li><li>Shipping</li><li>Returns</li><li>Ring Sizing</li><li>FAQ</li></ul>
      </div>
      <div>
        <h4>Call Now For Services</h4>
        <p class="phone" style="color:var(--ink)">(021) 555 0148</p>
        <div class="contact-line"><svg width="12" height="10" viewBox="0 0 12 10" fill="none" stroke="#2b2b2b"><rect x=".5" y=".5" width="11" height="9"/><path d="M.5.5L6 5l5.5-4.5"/></svg>Email Us</div>
        <div class="contact-line"><svg width="10" height="12" viewBox="0 0 10 12" fill="none" stroke="#2b2b2b"><path d="M5 11.5S1 7 1 4.5a4 4 0 0 1 8 0C9 7 5 11.5 5 11.5z"/><circle cx="5" cy="4.5" r="1.3"/></svg>Get Directions</div>
      </div>
    </div>
    <div class="copyright">© 2024 Lunelle Jewellery. All rights reserved.</div>
  </footer>

</div>
</body>
</html>
```